1200mm high x 900mm wide kids fitness poster for gym

I need an a poster designed to promote my kids/teenagers class.

This class is aimed at parents with kids between 10-15.

Design should be friendly and modern

Class is designed for kids that play sport and want to improve their fitness

Industry/Entity Type

Fitness

Font styles to use
Sans Serif

Colors

Designer to choose colors to be used in the design.

Requirements
Must have
• Text:
• Bright Stride teens program (TITLE)
• Improve: Performance, health, fitness, confidence, team mentality (BULLET POINTS)
• They will love our teen program! Contact us now to find out more:
• 1300452198
• enquiries@brightstride.fitness
• www.brightstride.fitness
• Must have friendly image of kids fitness or sport (FUN AND FRIENDLY IMAGE)

```html
<!DOCTYPE html>
<html lang="en">
<head>
<meta charset="utf-8">
<title>Bright Stride Teens Program Poster</title>
<link rel="stylesheet" href="https://fonts.googleapis.com/css2?family=Oswald:wght@500;600;700&family=Fredoka:wght@500;600&display=swap">
<style>
  :root {
    --navy: #123f86;
    --blue: #1f6fc4;
    --sky: #3a9be0;
    --ice: #e8f2fb;
    --paper: #f6f9fd;
    --ink: #0f2f63;
    --stage: #dfe3e8;
    --photo-a: #e9dccb;
    --photo-b: #c9a57f;
    --photo-c: #f4f1ec;
  }
  * { box-sizing: border-box; margin: 0; padding: 0; }
  html, body { width: 1080px; height: 1200px; overflow: hidden; background: var(--stage); }
  .poster {
    position: absolute; left: 90px; top: 0; width: 900px; height: 1200px; overflow: hidden;
    background: repeating-linear-gradient(170deg, var(--paper) 0 26px, var(--ice) 26px 52px);
    font-family: "Fredoka", "Arial Rounded MT Bold", sans-serif; color: var(--navy);
  }
  .hero-photo {
    position: absolute; left: 0; top: 0; width: 900px; height: 480px;
    background: linear-gradient(180deg, var(--photo-c) 0%, var(--photo-a) 45%, var(--photo-b) 100%);
    clip-path: polygon(0 0, 100% 0, 100% 80%, 0 100%);
  }
  .brand-tab { position: absolute; left: 0; top: 0; }
  .brand-name {
    position: absolute; left: 36px; top: 34px; display: flex; align-items: center; gap: 12px;
    font-family: "Oswald", sans-serif; font-weight: 600; font-size: 30px; color: #fff; letter-spacing: 1px;
  }
  .brand-dot { width: 18px; height: 18px; border-radius: 50%; background: #fff; }
  .accent-triangle { position: absolute; right: 60px; top: 40px; }
  .left-wedge { position: absolute; left: 0; top: 440px; }
  .title-ribbon {
    position: absolute; left: 140px; top: 455px; width: 720px; height: 96px;
    transform: rotate(-6deg); transform-origin: left center;
  }
  .title-ribbon .ribbon-back {
    position: absolute; inset: 12px -10px -12px 10px; border-radius: 48px; border: 4px solid var(--sky);
  }
  .title-ribbon .ribbon-face {
    position: absolute; inset: 0; border-radius: 48px; background: var(--navy);
    display: flex; align-items: center; justify-content: center;
    font-family: "Oswald", sans-serif; font-weight: 700; font-size: 46px; color: #fff; letter-spacing: 0.5px;
  }
  .benefit {
    position: absolute; display: flex; align-items: center; gap: 14px;
    font-weight: 600; font-size: 36px; line-height: 1; color: var(--navy); white-space: nowrap;
  }
  .benefit svg { flex: none; }
  .divider { position: absolute; left: 40px; top: 848px; }
  .photo-circle {
    position: absolute; border-radius: 50%; border: 6px solid var(--blue);
    background: radial-gradient(circle at 40% 40%, var(--photo-c), var(--photo-a) 55%, var(--photo-b));
  }
  .contact { position: absolute; left: 56px; top: 878px; }
  .contact-lead {
    font-family: "Oswald", sans-serif; font-weight: 600; font-size: 23px; line-height: 1.3;
    color: var(--ink); text-transform: uppercase;
  }
  .contact-line { display: flex; align-items: center; gap: 16px; margin-top: 10px; }
  .phone-number { font-family: "Oswald", sans-serif; font-weight: 700; font-size: 54px; line-height: 1.15; color: var(--navy); }
  .contact-detail { font-family: "Oswald", sans-serif; font-weight: 500; font-size: 24px; color: var(--ink); text-transform: uppercase; }
  .footer-band { position: absolute; left: 0; bottom: 0; }
  .footer-brand {
    position: absolute; right: 60px; bottom: 30px; display: flex; align-items: center; gap: 10px;
    font-family: "Oswald", sans-serif; font-weight: 600; font-size: 24px; color: var(--navy); letter-spacing: 1px;
  }
  .footer-brand .brand-dot { background: var(--navy); width: 14px; height: 14px; }
</style>
</head>
<body>
<main class="poster">
  <div class="hero-photo" role="img" aria-label="Photo of a coach guiding two smiling kids doing push-ups on a wooden gym floor"></div>

  <svg class="brand-tab" width="380" height="120" viewBox="0 0 380 120"><polygon points="0,0 380,0 320,110 0,110" fill="var(--navy)"/></svg>
  <div class="brand-name"><span class="brand-dot"></span>BRIGHT STRIDE</div>

  <svg class="accent-triangle" width="130" height="120" viewBox="0 0 130 120"><polygon points="20,110 120,0 110,110" fill="var(--blue)"/><polygon points="0,60 30,40 20,110" fill="var(--sky)" opacity="0.7"/></svg>

  <svg class="left-wedge" width="140" height="180" viewBox="0 0 140 180"><polygon points="0,40 140,20 0,180" fill="var(--navy)"/><polygon points="0,20 90,10 0,60" fill="var(--sky)"/></svg>

  <div class="title-ribbon">
    <div class="ribbon-back"></div>
    <h1 class="ribbon-face">BRIGHT STRIDE TEENS PROGRAM</h1>
  </div>

  <div class="benefit" style="left:60px; top:600px;">
    <svg width="52" height="52" viewBox="0 0 56 56"><polygon points="28,3 50,15 50,41 28,53 6,41 6,15" fill="#fff" stroke="var(--navy)" stroke-width="4"/><rect x="16" y="24" width="24" height="10" rx="4" fill="#e23b3b"/></svg>
    Performance
  </div>
  <div class="benefit" style="left:60px; top:685px;">
    <svg width="52" height="52" viewBox="0 0 56 56"><polygon points="28,3 50,15 50,41 28,53 6,41 6,15" fill="#fff" stroke="var(--navy)" stroke-width="4"/><rect x="14" y="22" width="28" height="12" rx="4" fill="#f2a53a"/></svg>
    Fitness
  </div>
  <div class="benefit" style="left:60px; top:770px;">
    <svg width="52" height="52" viewBox="0 0 56 56"><polygon points="28,3 50,15 50,41 28,53 6,41 6,15" fill="#fff" stroke="var(--navy)" stroke-width="4"/><circle cx="28" cy="28" r="11" fill="#e86a4a"/></svg>
    Team Mentality
  </div>
  <div class="benefit" style="left:480px; top:565px;">
    <svg width="52" height="52" viewBox="0 0 56 56"><polygon points="28,3 50,15 50,41 28,53 6,41 6,15" fill="#fff" stroke="var(--navy)" stroke-width="4"/><circle cx="28" cy="28" r="11" fill="#e23b3b"/></svg>
    Health
  </div>
  <div class="benefit" style="left:480px; top:650px;">
    <svg width="52" height="52" viewBox="0 0 56 56"><polygon points="28,3 50,15 50,41 28,53 6,41 6,15" fill="#fff" stroke="var(--navy)" stroke-width="4"/><circle cx="28" cy="28" r="11" fill="#f2b630"/></svg>
    Confidence
  </div>

  <svg class="divider" width="820" height="30" viewBox="0 0 820 30"><line x1="0" y1="4" x2="820" y2="4" stroke="var(--navy)" stroke-width="4"/><line x1="0" y1="14" x2="420" y2="14" stroke="var(--sky)" stroke-width="3"/><line x1="0" y1="24" x2="380" y2="24" stroke="var(--sky)" stroke-width="2"/></svg>

  <div class="photo-circle" style="left:470px; top:790px; width:125px; height:125px;" role="img" aria-label="Photo of kids stretching in a fitness class"></div>
  <div class="photo-circle" style="left:640px; top:735px; width:210px; height:210px;" role="img" aria-label="Photo of teens training together in a gym"></div>
  <div class="photo-circle" style="left:535px; top:935px; width:125px; height:125px;" role="img" aria-label="Photo of a coach and kid doing an exercise drill"></div>

  <section class="contact">
    <p class="contact-lead">They will love our teen program!<br>Contact us now to find out more:</p>
    <div class="contact-line">
      <svg width="44" height="44" viewBox="0 0 24 24"><path d="M6.6 10.8a15.1 15.1 0 0 0 6.6 6.6l2.2-2.2a1 1 0 0 1 1-.25 11.4 11.4 0 0 0 3.6.57 1 1 0 0 1 1 1V20a1 1 0 0 1-1 1A17 17 0 0 1 3 4a1 1 0 0 1 1-1h3.5a1 1 0 0 1 1 1c0 1.25.2 2.45.57 3.570a1 1 0 0 1-.25 1z" fill="none" stroke="var(--navy)" stroke-width="1.6"/></svg>
      <span class="phone-number">1300.452.198</span>
    </div>
    <div class="contact-line">
      <svg width="28" height="28" viewBox="0 0 24 24" fill="none" stroke="var(--navy)" stroke-width="2"><circle cx="12" cy="12" r="10"/><ellipse cx="12" cy="12" rx="4.5" ry="10"/><line x1="2" y1="12" x2="22" y2="12"/></svg>
      <span class="contact-detail">www.brightstride.fitness</span>
    </div>
    <div class="contact-line">
      <svg width="28" height="28" viewBox="0 0 24 24" fill="none" stroke="var(--navy)" stroke-width="2"><rect x="2" y="5" width="20" height="14" rx="2"/><polyline points="2,6 12,13 22,6"/></svg>
      <span class="contact-detail">enquiries@brightstride.fitness</span>
    </div>
  </section>

  <svg class="footer-band" width="900" height="110" viewBox="0 0 900 110"><path d="M0,96 H560 Q600,96 620,70 L640,46 Q655,30 680,30 H900 V110 H0 Z" fill="#fff"/><path d="M0,96 H560 Q600,96 620,70 L640,46 Q655,30 680,30 H900" fill="none" stroke="var(--blue)" stroke-width="5"/><rect x="0" y="100" width="900" height="10" fill="var(--navy)"/></svg>
  <div class="footer-brand"><span class="brand-dot"></span>BRIGHT STRIDE</div>
</main>
</body>
</html>
```